3D Packaging Design - Wine In Box

Need to create premium packaging for our wine-in-a-box brand - OpenCask Wines. We offer Properly Fine Coastal Vintage – In a Carton’
(Need to receive 3D rendered files that look like a printed product that we can use on a landing page for our website... also to be supplied to our printer).

We are a premium wine brand - exploring Australia's wine regions and delivering the best 'drink now' wines seasonally to your door.

See brightfernly.com.au for a good example of wine in a box done minimalistically/modernly - similar to what we would like.

Our font is Garet Extra Bold
Subfont is Majesty

Main brand colour is #8d0345
Could also use #E8cdd7 and #747629 or #c4c676; possibly black or grey #777779

We want a package that is minimalistic and modern, more serious than playful, more masculine than feminine.

Would like to see the words OPENCASK running up the side of the box - going over the edge (i.e., the top half of the words on one side of the box, the bottom half of the words on the other side of the box). Maybe with white negative space around the logo – with the rest of the box a neutral (or brand colour) package.

We would want the type of grape displayed prominently -
CHARDONNAY
Yarra Valley, 2022
Winemaker: Dellwyn
to run on the 'label' of the box.

Needs to have a place to put wine information (legal info) plus info about the wine on back side of label along with a prominent QR code on the back label that can take them to 'more'.

Image of a competitive produce (Bright Fernly) included. Something similar - I like the idea of a more 'shimmery' or textured paper used in the packaging; but also a black box might exude premium and interesting to see? - something that will look premium - and look good on instagram - as the produce will be sold entirely online (examples of black bottles and boxes included to give an idea of that approach).

Ideally our 'label' will not run across the words OPENCASK (like their’s does). But the label changes with each wine we release so may need to be applied by a sticker like traditional wine bottles (not printed on the box). (Bright Fernly prints on a paper sleeve that goes around the box); need to leave space for us to do the same.

Box dimensions approx. 27x8x13.5

Target audience:
Educated wine drinkers (primarily males) - 28-40.
Mainly urban - (Sydney, Melbourne); incomes $75,000+
Wine educated... or want to be.

Use our sketch as the guidelines - but open to artistic interpretation - something make a bit 'edgier' than what we've shared in addition to a mockup of what we've sketched. Would like to see designs that emulate our mock up; but also options that might be a good bit different tan what's in our heads.

Target Market(s)

Educated wine drinkers (primarily males) - 28-40. Mainly urban - (Sydney, Melbourne); incomes $75,000+ Wine educated... or want to be.

Industry/Entity Type

Wine Industry

Font styles to use
Other font styles liked:
• Garet Fonts (i.e., Garet Extra Bold for writing along side of box.) 'Wines' of our logo is in Majesty - that might look nice on front of package in smaller font size at top of the word OPENCASK.

Colors

Designer to choose colors to be used in the design.

Requirements
Must have
• Must use the colours included in the project description in conjunction with neutrals and negative space. We would like to minimize printing costs - so red wines to go in a red printed box; white wines in a white printed box, rose wines into a light pink printed box (see colours supplied).
Nice to have
• Check out BrightFernly.com.au and Pourmerit.com

```html
<!DOCTYPE html>
<html lang="en">
<head>
<meta charset="utf-8">
<title>OpenCask Wines – Chardonnay Carton Artwork</title>
<link rel="stylesheet" href="https://fonts.googleapis.com/css2?family=Archivo+Black&family=Montserrat:wght@300;400;800&display=swap">
<style>
  :root {
    --backdrop: #e9cdd7;
    --brand: #8d1147;
    --brand-deep: #7b0d3c;
    --paper: #ffffff;
    --ink: #3a2a30;
  }
  html, body {
    margin: 0;
    width: 1200px;
    height: 1200px;
    overflow: hidden;
    background: var(--backdrop);
  }
  .artwork { display: block; width: 1200px; height: 1200px; }
  .carton-shadow { filter: drop-shadow(0 10px 14px rgba(90, 20, 50, 0.35)); }
  .panel-main { fill: var(--brand); }
  .panel-edge { fill: var(--brand-deep); }
  .label-card { fill: var(--paper); }
  .wordmark {
    font-family: "Archivo Black", sans-serif;
    font-size: 92px;
    fill: var(--paper);
  }
  .wordmark-sub {
    font-family: "Montserrat", sans-serif;
    font-weight: 300;
    font-size: 54px;
    fill: var(--paper);
  }
  .varietal {
    font-family: "Montserrat", sans-serif;
    font-weight: 800;
    font-size: 16px;
    letter-spacing: 0.3px;
    fill: var(--brand);
  }
  .vintage-line {
    font-family: "Montserrat", sans-serif;
    font-weight: 400;
    font-size: 12px;
    fill: var(--brand);
  }
  .back-copy {
    font-family: "Montserrat", sans-serif;
    font-weight: 400;
    font-size: 6.3px;
    fill: var(--ink);
  }
</style>
</head>
<body>
<svg class="artwork" viewBox="0 0 1200 1200" xmlns="http://www.w3.org/2000/svg">
  <defs>
    <clipPath id="front-face"><rect x="132" y="304" width="467" height="586"/></clipPath>
    <clipPath id="back-face"><rect x="599" y="304" width="468" height="586"/></clipPath>
  </defs>

  <g class="carton-shadow">
    <!-- front face -->
    <rect class="panel-main" x="132" y="304" width="467" height="586"/>
    <rect class="panel-edge" x="132" y="304" width="172" height="586"/>
    <!-- back face -->
    <rect class="panel-main" x="599" y="304" width="468" height="586"/>
    <rect class="panel-edge" x="599" y="304" width="174" height="586"/>
  </g>

  <!-- front face branding -->
  <g clip-path="url(#front-face)">
    <text class="wordmark" transform="translate(346 893) rotate(-90)" textLength="592" lengthAdjust="spacingAndGlyphs">OPENCASK</text>
    <text class="wordmark-sub" transform="translate(412 534) rotate(-90)" textLength="210" lengthAdjust="spacingAndGlyphs">Wines</text>
  </g>

  <!-- front label -->
  <rect class="label-card" x="430" y="699" width="169" height="146"/>
  <text class="varietal" x="584" y="797" text-anchor="end">CHARDONNAY</text>
  <text class="vintage-line" x="584" y="814" text-anchor="end">Yarra Valley, 2022</text>
  <text class="vintage-line" x="584" y="831" text-anchor="end">Winemaker: Dellwyn</text>

  <!-- back face branding -->
  <g clip-path="url(#back-face)">
    <text class="wordmark" transform="translate(815 893) rotate(-90)" textLength="592" lengthAdjust="spacingAndGlyphs">OPENCASK</text>
    <text class="wordmark-sub" transform="translate(880 534) rotate(-90)" textLength="210" lengthAdjust="spacingAndGlyphs">Wines</text>
  </g>

  <!-- back label -->
  <rect class="label-card" x="912" y="699" width="155" height="146"/>
  <text class="back-copy" x="928" y="766">
    <tspan x="928" dy="0">Lorem ipsum dolor sit amet, conse-</tspan>
    <tspan x="928" dy="9.3">cLorem ipsum dolor sit amet, consec-</tspan>
    <tspan x="928" dy="9.3">tetuer adipiscing elit, sed diam</tspan>
    <tspan x="928" dy="9.3">nonummy nibh Lorem ipsum dolor sit</tspan>
    <tspan x="928" dy="9.3">amet, consectetuer adipiscing elit,</tspan>
    <tspan x="928" dy="9.3">sed diam nonummy nibh euismod</tspan>
    <tspan x="928" dy="9.3">tincidunt ut laoreet dolore magna</tspan>
    <tspan x="928" dy="9.3">aliquam erat volutpat. Ut wisi enim</tspan>
  </text>
</svg>
</body>
</html>
```